Business Card for a Wellness and Aesthetic Center

I'd like to have a business card design for a Wellness and Aesthetic Center based in the Philippines called "Tidelark Wellness and Aesthetic Inc." They provide services such as medical and aesthetic dermatology. Specializing on cosmetic and anti-aging procedures.

The target market of the business is mostly women from the upper class from 30 to 60 years old.

The feel and look of the card should be feminine, modern, minimalist and classy.

The colors to play with are gold and black.

The front part should contain:
- Name (example: Marisol Tebenay Quiroga, MD)
- Designation (example: Medical Director)
- Company Logo

The back part should contain:
- Company Logo
- Address
- Contact Details
- Website

For more details and inspiration you may visit their website at http://tidelarkph.com/

Thank you very much!

Target Market(s)

Women from the upper class from 30 to 60 years old.

Industry/Entity Type

Business

Contact Information for Business Card

- Company Logo

- Company Logo
- Address
- Contact Details
- Website

Font styles to use
Serif
Script

Colors
ffc214
fece3e
faa54b
f78f20
000000

Requirements
Must have
• Design should be feminine, modern, minimalist/simple and classy.
Nice to have
• You can play with lines, curves, gardient and be creative on the placement of texts and logo.
Should not have
• Pictures like body, face or nature scene.

```html
<!DOCTYPE html>
<html lang="en">
<head>
<meta charset="utf-8">
<title>Tidelark Wellness and Aesthetic Inc. – Business Card</title>
<link rel="stylesheet" href="https://fonts.googleapis.com/css2?family=Alegreya:wght@400;500&display=swap">
<style>
  :root {
    --page-bg: #e9e4dc;
    --card-black: #000000;
    --gold: #f0961e;
    --gold-soft: #faa54b;
    --ink-light: #f2f2f2;
    --card-shadow: rgba(0, 0, 0, 0.28);
  }
  * { margin: 0; padding: 0; box-sizing: border-box; }
  html, body {
    width: 1200px;
    height: 900px;
    overflow: hidden;
    background: var(--page-bg);
  }
  .canvas {
    position: relative;
    width: 1200px;
    height: 900px;
    font-family: "Alegreya", Georgia, serif;
  }
  .card {
    position: absolute;
    width: 580px;
    height: 330px;
    background: var(--card-black);
    border-radius: 4px;
    box-shadow: 0 14px 30px var(--card-shadow);
  }
  .card--back { left: 110px; top: 100px; }
  .card--front { left: 510px; top: 470px; }

  .brand-mark {
    position: absolute;
    display: flex;
    align-items: center;
    gap: 10px;
    color: var(--gold);
    font-size: 30px;
    font-weight: 400;
    letter-spacing: 0.5px;
  }
  .brand-mark__dot {
    width: 12px;
    height: 12px;
    border-radius: 50%;
    background: var(--gold);
  }
  .card--back .brand-mark { left: 50%; top: 78px; transform: translateX(-50%); }
  .card--front .brand-mark { right: 56px; top: 74px; }

  .contact-block {
    position: absolute;
    left: 46px;
    bottom: 42px;
    color: var(--ink-light);
    font-size: 17px;
    line-height: 1.55;
  }
  .contact-block .label { color: var(--gold); }
  .contact-block .web { color: var(--gold); margin-left: 12px; }
  .contact-block .gap { margin-left: 12px; }

  .person {
    position: absolute;
    left: 52px;
    top: 168px;
  }
  .person__name {
    color: var(--gold);
    font-size: 33px;
    font-weight: 400;
    line-height: 1.1;
  }
  .person__role {
    color: var(--ink-light);
    font-size: 19px;
    margin-top: 2px;
    margin-left: 10px;
  }
</style>
</head>
<body>
<main class="canvas">
  <section class="card card--back" aria-label="Card back">
    <div class="brand-mark"><span class="brand-mark__dot"></span>Tidelark</div>
    <address class="contact-block" style="font-style: normal;">
      <div>1234, Address GoesHere, Country, 12345</div>
      <div><span class="label">T:</span> (044) 123 456 789<span class="gap"><span class="label">F:</span> (044) 123456789</span><span class="gap"><span class="label">M:</span> (044)123456789</span></div>
      <div><span class="label">E:</span> info@youremail.com<span class="web">www.yourweb.com</span></div>
    </address>
  </section>

  <section class="card card--front" aria-label="Card front">
    <div class="brand-mark"><span class="brand-mark__dot"></span>Tidelark</div>
    <div class="person">
      <h1 class="person__name">Jonathan Smith</h1>
      <p class="person__role">Managing Director</p>
    </div>
  </section>
</main>
</body>
</html>
```